Independent Artist - Album Cover Design

I need a full album cover design for my debut album Velvet After Dark. The album is a love-inspired, passionate, soulful, relationship laden album. An album that can relate to anyone in love (or lust/obsession), going through ups and downs of relationships,and overcoming any hardships and enjoying the joys of true love, sex, and companionship. My first thoughts are a black and white design with the color red poppin off in there maybe in some of the lettering but I am open to some creative ideas. Looking for something clean and sexy that represents what the album is about. I was thinking maybe having a photo of myself on there but don't really have any that would work Stay Late but I can take some and send a link if you have some good ideas.

My Artist name if I didnt mention before is Velmora. I would like that on the album cover as well. Also I need a full album cover Front and Back. Below is the track list if you could incorporate that as well. And below is also a link to some photos. Thank you.

https://www.filecrate-demo.net/sh/qk4rmvplwex7dan/TyuNpoeRkW

1 .Silk Skin (Feat. Marlon Quickstep)
2.  Midnight Heat (Feat. Dolo Vey)
3 .Feel The Wave (Feat. Tumo)
4 . Hold Me Closer
5. Sidewayz
6.  For Us (Feat. Dolo Vey)
7 .She Fits Right In Here
8 . Stay Late
9 . Weekend Is Ours
10.  Down This Hall
11.  We Might
12 . Seasons Of Desire

New Clearer Pictures Posted to filecrate folder. Thanks.

https://www.filecrate-demo.net/sh/qk4rmvplwex7dan/KKRm5t71hZyWqNofBxeLuvcsn

```html
<!DOCTYPE html>
<html lang="en">
<head>
<meta charset="utf-8">
<title>Velmora – Velvet After Dark – Album Package</title>
<link href="https://fonts.googleapis.com/css2?family=Russo+One&family=Raleway:wght@400;600&display=swap" rel="stylesheet">
<style>
:root{
  --bg:#b3b3b3;
  --panel:#050505;
  --ink:#f2f2f2;
  --ink-soft:#c9c9c9;
  --ink-dim:#9a9a9a;
  --photo-light:#7a7a7a;
  --photo-mid:#2e2e2e;
  --photo-warm:#8a3218;
  --disc-edge:#6e6e6e;
  --disc-band:#0d0d10;
}
*{margin:0;padding:0;box-sizing:border-box}
html,body{width:1200px;height:750px;overflow:hidden;background:var(--bg)}
body{position:relative;font-family:"Raleway",sans-serif;color:var(--ink)}
.panel{position:absolute;background:var(--panel);overflow:hidden}
.front{left:13px;top:12px;width:360px;height:356px}
.back{left:380px;top:12px;width:440px;height:357px}
.booklet{left:825px;top:12px;width:363px;height:356px}

.photo{position:absolute;top:0}
.front .photo{left:50px;width:260px;height:356px;
  background:
    radial-gradient(ellipse 45% 35% at 30% 82%,rgba(138,50,24,.75),rgba(138,50,24,0) 100%),
    radial-gradient(ellipse 45% 60% at 50% 32%,var(--photo-light),var(--photo-mid) 60%,var(--panel) 100%)}
.back .photo{left:26px;width:200px;height:357px;
  background:
    radial-gradient(ellipse 55% 35% at 30% 72%,rgba(138,50,24,.75),rgba(138,50,24,0) 100%),
    radial-gradient(ellipse 50% 60% at 55% 35%,var(--photo-light),var(--photo-mid) 60%,var(--panel) 100%)}

.wordmark{position:absolute;font-family:"Russo One",sans-serif;font-weight:400;color:var(--ink);letter-spacing:1px;white-space:nowrap}
.front .wordmark{left:0;width:360px;text-align:center;top:276px;font-size:40px}
.front .album-title{position:absolute;left:0;width:360px;text-align:center;top:320px;font-size:13px;letter-spacing:5px;color:var(--ink-soft);white-space:nowrap}

.spine{position:absolute;top:0;height:357px;width:26px}
.spine-left{left:0}
.spine-right{right:0;background:#000}
.spine span{position:absolute;left:50%;white-space:nowrap;font-size:11px;letter-spacing:1px}
.spine-left .title{top:75px;transform:translate(-50%,-50%) rotate(-90deg);color:var(--ink-soft)}
.spine-left .artist{top:272px;transform:translate(-50%,-50%) rotate(-90deg);font-weight:600}
.spine-right .artist{top:55px;transform:translate(-50%,-50%) rotate(90deg);font-weight:600}
.spine-right .title{top:262px;transform:translate(-50%,-50%) rotate(90deg);color:var(--ink-soft)}

.tracklist{position:absolute;left:214px;top:36px;list-style:none;font-size:8px;line-height:11.7px;letter-spacing:.4px;color:var(--ink-soft);white-space:nowrap}
.tracklist .no{display:inline-block;width:20px}
.back .wordmark{left:214px;top:209px;font-size:30px}
.credits{position:absolute;left:214px;top:258px;font-size:6.5px;line-height:9px;letter-spacing:.4px;color:var(--ink-soft);white-space:nowrap}
.credits b{font-weight:600;color:var(--ink)}
.links{position:absolute;left:66px;top:327px;width:342px;display:flex;justify-content:space-between;font-size:5px;letter-spacing:.2px;color:var(--ink-dim);white-space:nowrap}

.thanks{position:absolute;left:47px;top:52px;width:240px;font-size:5.6px;line-height:7.4px;letter-spacing:.3px;color:var(--ink-soft);text-align:justify}
.thanks h2{font-size:6px;font-weight:600;color:var(--ink);margin-bottom:3px}
.thanks p{margin-bottom:7px}

.disc{position:absolute;left:13px;top:378px}
.disc text{font-family:"Raleway",sans-serif}
.disc .disc-wordmark{font-family:"Russo One",sans-serif}
</style>
</head>
<body>

<section class="panel front">
  <div class="photo" role="img" aria-label="Black and white portrait of the artist in a hat and tank top, wrapped in smoke with warm red light at the lower left"></div>
  <h1 class="wordmark">VELMORA</h1>
  <p class="album-title">VELVET AFTER DARK</p>
</section>

<section class="panel back">
  <div class="spine spine-left"><span class="title">VELVET AFTER DARK</span><span class="artist">VELMORA</span></div>
  <div class="photo" role="img" aria-label="Black and white photo of the artist with a tattooed arm, leaning forward in smoke with warm red light"></div>
  <ol class="tracklist">
    <li><span class="no">01.</span>SILK SKIN (FEAT. MARLON QUICKSTEP)</li>
    <li><span class="no">02.</span>MIDNIGHT HEAT (FEAT. DOLO VEY)</li>
    <li><span class="no">03.</span>FEEL THE WAVE (FEAT. TUMO)</li>
    <li><span class="no">04.</span>HOLD ME CLOSER</li>
    <li><span class="no">05.</span>SIDEWAYZ</li>
    <li><span class="no">06.</span>FOR US (FEAT. DOLO VEY)</li>
    <li><span class="no">07.</span>SHE FITS RIGHT IN HERE</li>
    <li><span class="no">08.</span>STAY LATE (FEAT. DOLO VEY)</li>
    <li><span class="no">09.</span>WEEKEND IS OURS</li>
    <li><span class="no">10.</span>DOWN THIS HALL</li>
    <li><span class="no">11.</span>WE MIGHT</li>
    <li><span class="no">12.</span>SEASONS OF DESIRE</li>
  </ol>
  <h2 class="wordmark">VELMORA</h2>
  <p class="credits"><b>SPECIAL TAHNKS</b><br>PRODUCERS: VELMORA, ROOK BEATS FEATURED<br>ARTIST: DOLO VEY, MARLON QUICKSTEP, TUMO 7</p>
  <div class="links"><span>WWW.SOUNDVAULT-DEMO.COM/VELMORA</span><span>WWW.VELMORAMUSIC-DEMO.COM</span><span>WWW.TRACKLANE-DEMO.COM/NIGHTOWL</span></div>
  <div class="spine spine-right"><span class="artist">VELMORA</span><span class="title">VELVET AFTER DARK</span></div>
</section>

<section class="panel booklet">
  <div class="thanks">
    <h2>SPECIAL THANKS:</h2>
    <p>WANT TO GIVE A SPECIAL THANKS TO EVERYONE THAT MADE THIS ALBUM POSSIBLE. TO MY FAMILY THANK YOU FOR YOUR SUPPORT AND LETTING ME TAKE THE TIME I NEEDED IN THE STUDIO TO FOCUS ON THE ALBUM. I COULDN'T HAVE COMPLETED THIS ALBUM WITHOUT THAT SUPPORT.</p>
    <p>TO TUMO, ROOK BEATS, DOLO VEY AND MARLON QUICKSTEP THANK YOU FOR TAKING THE TIME TO WRITE, RECORD, AND PRODUCE SOLID TRACKS FOR THIS ALBUM. YOUR TALENT SHOWS AND I APPRECIATE YOU GUYS TAKING THE TIME TO BE A PART OF MY DREAM AND MAKE IT BECOME A REALITY.</p>
    <p>MUCH LOVE</p>
  </div>
</section>

<svg class="disc" width="360" height="360" viewBox="0 0 360 360" aria-label="Disc label">
  <defs>
    <clipPath id="disc-clip"><circle cx="180" cy="180" r="179"/></clipPath>
    <path id="disc-rim" d="M12 180 A168 168 0 0 0 348 180"/>
  </defs>
  <circle cx="180" cy="180" r="179" fill="#050505" stroke="var(--disc-edge)" stroke-width="1"/>
  <g clip-path="url(#disc-clip)">
    <rect x="0" y="187" width="282" height="173" fill="var(--disc-band)"/>
  </g>
  <text x="180" y="87" text-anchor="middle" fill="#f2f2f2" font-size="11" letter-spacing="5" font-weight="600">VELVET AFTER DARK</text>
  <text class="disc-wordmark" x="180" y="299" text-anchor="middle" fill="#f2f2f2" font-size="30">VELMORA</text>
  <g fill="#9a9a9a" font-size="6" letter-spacing=".5">
    <text><textPath href="#disc-rim" startOffset="5%">WWW.SOUNDVAULT-DEMO.COM/VELMORA</textPath></text>
    <text text-anchor="middle"><textPath href="#disc-rim" startOffset="50%">WWW.VELMORAMUSIC-DEMO.COM</textPath></text>
    <text text-anchor="end"><textPath href="#disc-rim" startOffset="95%">WWW.TRACKLANE-DEMO.COM/NIGHTOWL</textPath></text>
  </g>
</svg>

</body>
</html>
```